Wall Word Art for tree care company to brand core values at the business

I am looking to have some wall art designed base on our companies core values and passion to be displayed around our office walls.

1. Grow and develop our team to win
2. competitive - value in a goal and purpose. not just about winning...its about the process. Iron sharpens Iron
3. Open & Honest - sharing the storyline. yes is our yes. no is our no. vulnerable.
4. Accountable - celebrating the wins & addressing the opportunities. hold each other to a standard, with grace.
5. Professional - a pro's-pro. how we communicate, look and act.
6. Growing Relationships through trees.

Target Market(s)

our employees

Industry/Entity Type

tree care

Other font styles liked:
• montserrat

Requirements
Must have
• brand colors and font
Nice to have
• incorporate icons and logo, or create new icons

```html
<!DOCTYPE html>
<html lang="en">
<head>
<meta charset="utf-8">
<title>Alder Tree Care — Core Values Wall Art</title>
<link href="https://fonts.googleapis.com/css2?family=Montserrat:wght@400;600;700&display=swap" rel="stylesheet">
<style>
  :root {
    --brand-red: #c41e2e;
    --brand-orange: #e8691e;
    --orange-tint: #fbe6d8;
    --card-bg: #f9f9f9;
    --card-edge: #cfcfcf;
    --page-bg: #ffffff;
    --caption: #6a6a6a;
  }
  * { box-sizing: border-box; margin: 0; padding: 0; }
  html, body {
    width: 1200px;
    height: 2957px;
    overflow: hidden;
    background: var(--page-bg);
    font-family: "Montserrat", Arial, sans-serif;
  }
  .wall-set { position: relative; width: 1200px; height: 2957px; }
  .value-card {
    position: absolute;
    left: 218px;
    width: 765px;
    height: 510px;
    background: var(--card-bg);
    border-bottom: 2px solid var(--card-edge);
    border-right: 1px solid #e4e4e4;
  }
  .brand-name {
    position: absolute;
    left: 24px;
    top: 30px;
    display: flex;
    align-items: center;
    gap: 6px;
    color: var(--brand-red);
    font-weight: 700;
    font-size: 25px;
    letter-spacing: -0.01em;
  }
  .brand-dot {
    width: 10px; height: 10px;
    border-radius: 50%;
    background: var(--brand-red);
  }
  .value-title {
    position: absolute;
    left: 0; right: 0;
    bottom: 315px;
    text-align: center;
    color: var(--brand-red);
    font-weight: 700;
    text-transform: uppercase;
    letter-spacing: 0.1em;
    line-height: 1.22;
  }
  .value-title .headline { display: block; font-size: 31px; }
  .value-title .tagline { display: block; font-size: 27px; }
  .value-arc {
    position: absolute;
    left: 210px;
    top: 208px;
    width: 345px;
    height: 26px;
  }
  .value-badge {
    position: absolute;
    left: 309px;
    top: 227px;
    width: 146px;
    height: 146px;
  }
  .value-caption {
    position: absolute;
    left: 0; right: 0;
    top: 390px;
    text-align: center;
    font-size: 15px;
    font-weight: 400;
    color: var(--caption);
    letter-spacing: 0.01em;
  }
  .corner-mark {
    position: absolute;
    left: 697px;
    top: 449px;
    width: 36px;
    height: 36px;
    border-radius: 50%;
    background: var(--brand-red);
  }
</style>
</head>
<body>
<main class="wall-set">

  <section class="value-card" style="top:115px">
    <div class="brand-name"><span class="brand-dot"></span>ALDER</div>
    <h2 class="value-title">
      <span class="headline">Accountable</span>
      <span class="tagline">Celebrating wins &amp;</span>
      <span class="tagline">addressing opportnities</span>
    </h2>
    <svg class="value-arc" viewBox="0 0 345 26"><path d="M2 24 Q172 -8 343 24" fill="none" stroke="var(--brand-red)" stroke-width="4" stroke-linecap="round"/></svg>
    <svg class="value-badge" viewBox="0 0 146 146">
      <circle cx="73" cy="73" r="70" fill="none" stroke="var(--brand-orange)" stroke-width="5"/>
      <circle cx="73" cy="73" r="62" fill="none" stroke="var(--brand-orange)" stroke-width="2"/>
      <circle cx="73" cy="73" r="50" fill="var(--orange-tint)" role="img" aria-label="Line icon of a balance scale with a laurel wreath and a puzzle piece"/>
    </svg>
    <p class="value-caption">Holding each other to a standard, with grace</p>
    <div class="corner-mark"></div>
  </section>

  <section class="value-card" style="top:683px">
    <div class="brand-name"><span class="brand-dot"></span>ALDER</div>
    <h2 class="value-title">
      <span class="headline">Professional</span>
      <span class="tagline">A pro’s pro</span>
    </h2>
    <svg class="value-arc" viewBox="0 0 345 26"><path d="M2 24 Q172 -8 343 24" fill="none" stroke="var(--brand-red)" stroke-width="4" stroke-linecap="round"/></svg>
    <svg class="value-badge" viewBox="0 0 146 146">
      <circle cx="73" cy="73" r="70" fill="none" stroke="var(--brand-orange)" stroke-width="5"/>
      <circle cx="73" cy="73" r="62" fill="none" stroke="var(--brand-orange)" stroke-width="2"/>
      <circle cx="73" cy="73" r="50" fill="var(--orange-tint)" role="img" aria-label="Line icon of a shield framing a professional in a suit"/>
    </svg>
    <p class="value-caption">Communicating, looking and acting with excellence</p>
    <div class="corner-mark"></div>
  </section>

  <section class="value-card" style="top:1250px">
    <div class="brand-name"><span class="brand-dot"></span>ALDER</div>
    <h2 class="value-title">
      <span class="headline">Open &amp; Honest</span>
      <span class="tagline">Yes is our yes. No is to no.</span>
    </h2>
    <svg class="value-arc" viewBox="0 0 345 26"><path d="M2 24 Q172 -8 343 24" fill="none" stroke="var(--brand-red)" stroke-width="4" stroke-linecap="round"/></svg>
    <svg class="value-badge" viewBox="0 0 146 146">
      <circle cx="73" cy="73" r="70" fill="none" stroke="var(--brand-orange)" stroke-width="5"/>
      <circle cx="73" cy="73" r="62" fill="none" stroke="var(--brand-orange)" stroke-width="2"/>
      <circle cx="73" cy="73" r="50" fill="var(--orange-tint)" role="img" aria-label="Line icon of two speech bubbles with a tick and a cross above a handshake"/>
    </svg>
    <p class="value-caption">Building trust through clear communication</p>
    <div class="corner-mark"></div>
  </section>

  <section class="value-card" style="top:1818px">
    <div class="brand-name"><span class="brand-dot"></span>ALDER</div>
    <h2 class="value-title">
      <span class="headline">Competitive</span>
      <span class="tagline">Iron sharpens iron</span>
    </h2>
    <svg class="value-arc" viewBox="0 0 345 26"><path d="M2 24 Q172 -8 343 24" fill="none" stroke="var(--brand-red)" stroke-width="4" stroke-linecap="round"/></svg>
    <svg class="value-badge" viewBox="0 0 146 146">
      <circle cx="73" cy="73" r="70" fill="none" stroke="var(--brand-orange)" stroke-width="5"/>
      <circle cx="73" cy="73" r="62" fill="none" stroke="var(--brand-orange)" stroke-width="2"/>
      <circle cx="73" cy="73" r="50" fill="var(--orange-tint)" role="img" aria-label="Line icon of two interlocking gears with spark lines"/>
    </svg>
    <p class="value-caption">Refining excellence through process</p>
    <div class="corner-mark"></div>
  </section>

  <section class="value-card" style="top:2386px">
    <div class="brand-name"><span class="brand-dot"></span>ALDER</div>
    <h2 class="value-title">
      <span class="headline">Grow and develop</span>
      <span class="headline">our team to win</span>
    </h2>
    <svg class="value-arc" viewBox="0 0 345 26"><path d="M2 24 Q172 -8 343 24" fill="none" stroke="var(--brand-red)" stroke-width="4" stroke-linecap="round"/></svg>
    <svg class="value-badge" viewBox="0 0 146 146">
      <circle cx="73" cy="73" r="70" fill="none" stroke="var(--brand-orange)" stroke-width="5"/>
      <circle cx="73" cy="73" r="62" fill="none" stroke="var(--brand-orange)" stroke-width="2"/>
      <circle cx="73" cy="73" r="50" fill="var(--orange-tint)" role="img" aria-label="Line icon of a team gathered around a growing sprout with upward arrows"/>
    </svg>
    <p class="value-caption">Building strength from the roots up</p>
    <div class="corner-mark"></div>
  </section>

</main>
</body>
</html>
```